Alcohol brand needs design for gift tin packaging

We need a new design for the gift tins for our vodka brand. The bottles are in the shape of an oil barrel and the tins are also in the same shape. We would like to see the use of our logo. The gift tin needs to have a premium look.
Images of our bottles, logo and the gift tin are attached.

```html
<!DOCTYPE html>
<html lang="en">
<head>
<meta charset="utf-8">
<title>Iron Drum Vodka – Gift Tin Wrap</title>
<link rel="stylesheet" href="https://fonts.googleapis.com/css2?family=Staatliches&family=Cinzel:wght@700&display=swap">
<style>
  :root {
    --page: #ffffff;
    --rust-deep: #2a140a;
    --rust-mid: #4a2412;
    --rust-warm: #5e2f15;
    --soot: #000000;
    --copper: #c0672c;
    --copper-dim: #a65a28;
  }
  html, body {
    margin: 0;
    padding: 0;
    width: 1200px;
    height: 1059px;
    overflow: hidden;
    background: var(--page);
  }
  .canvas {
    position: relative;
    width: 1200px;
    height: 1059px;
  }
  .tin-wrap {
    position: absolute;
    left: 63px;
    top: 300px;
    width: 1078px;
    height: 459px;
    overflow: hidden;
    background:
      radial-gradient(ellipse 30% 40% at 20% 55%, var(--soot) 0%, rgba(0,0,0,0.85) 45%, transparent 100%),
      radial-gradient(ellipse 26% 45% at 50% 60%, var(--soot) 0%, rgba(0,0,0,0.9) 55%, transparent 100%),
      radial-gradient(ellipse 28% 42% at 78% 50%, var(--soot) 0%, rgba(0,0,0,0.85) 50%, transparent 100%),
      radial-gradient(ellipse 20% 30% at 97% 62%, rgba(0,0,0,0.8) 0%, transparent 100%),
      radial-gradient(ellipse 40% 20% at 35% 10%, var(--rust-warm) 0%, transparent 100%),
      radial-gradient(ellipse 40% 20% at 60% 92%, var(--rust-warm) 0%, transparent 100%),
      linear-gradient(180deg, var(--rust-mid) 0%, var(--rust-deep) 50%, var(--rust-mid) 100%);
  }
  .brand-title {
    position: absolute;
    left: 0;
    right: 0;
    margin: 0;
    text-align: center;
    font-family: "Staatliches", "Impact", sans-serif;
    font-weight: 400;
    color: var(--copper);
    line-height: 1;
  }
  .brand-title .line-one {
    position: absolute;
    left: 0;
    right: 0;
    top: 26px;
    font-size: 64px;
    letter-spacing: 2px;
  }
  .brand-title .line-two {
    position: absolute;
    left: 0;
    right: 0;
    top: 92px;
    font-size: 56px;
    letter-spacing: 2px;
  }
  .brand-mark {
    position: absolute;
    left: 449px;
    top: 196px;
    width: 180px;
    height: 80px;
    display: flex;
    flex-direction: column;
    align-items: center;
    justify-content: center;
    gap: 8px;
  }
  .brand-mark .mark-dot {
    width: 22px;
    height: 22px;
    border-radius: 50%;
    background: var(--copper);
  }
  .brand-mark .mark-name {
    font-family: "Staatliches", "Impact", sans-serif;
    font-size: 30px;
    color: var(--copper);
    letter-spacing: 2px;
    line-height: 1;
  }
  .tagline {
    position: absolute;
    left: 0;
    right: 0;
    top: 412px;
    margin: 0;
    text-align: center;
    font-family: "Cinzel", "Times New Roman", serif;
    font-weight: 700;
    font-size: 17px;
    letter-spacing: 1.5px;
    word-spacing: 12px;
    color: var(--copper-dim);
  }
</style>
</head>
<body>
  <main class="canvas">
    <section class="tin-wrap" aria-label="Gift tin wrap, flat">
      <h1 class="brand-title">
        <span class="line-one">Iron Drum</span>
        <span class="line-two">Vodka</span>
      </h1>
      <div class="brand-mark">
        <span class="mark-dot"></span>
        <span class="mark-name">Iron Drum</span>
      </div>
      <p class="tagline">PREMIUM AUSTRALIAN VODKA</p>
    </section>
  </main>
</body>
</html>
```